Billboard Design for Equipment Rental Business

We need a billboard design for our equipment rental business called Brindlewood Equipment Company. We are based in Georgia. We rent construction tools, equipment, and dumpsters. We currently have a design but feel like we could get something better. Our phone number is 912-730-2591 and our website is www.brindlewoodequipment-example.com

```html
<!DOCTYPE html>
<html lang="en">
<head>
<meta charset="utf-8">
<title>Brindlewood Equipment Company – Billboard</title>
<link href="https://fonts.googleapis.com/css2?family=Montserrat:wght@600;700;800&family=Oswald:wght@500;600&family=Rubik:wght@600;800&family=Roboto+Condensed:wght@700&display=swap" rel="stylesheet">
<style>
  :root {
    --yellow: #f8b719;
    --ink: #1d1d1d;
    --panel: #202020;
    --white: #ffffff;
    --photo-light: #e6e6e6;
    --photo-mid: #cfcfcf;
    --page: #eceef1;
  }
  * { margin: 0; padding: 0; box-sizing: border-box; }
  html, body {
    width: 1200px; height: 785px; overflow: hidden;
    background: var(--page);
  }
  .billboard {
    position: absolute; left: 20px; top: 211px;
    width: 1160px; height: 362px;
    overflow: hidden; background: var(--white);
    box-shadow: 0 6px 24px rgba(0,0,0,.18);
  }
  .billboard__shapes { position: absolute; inset: 0; }
  .site-photo {
    position: absolute; inset: 0;
    clip-path: polygon(0 0, 700px 0, 530px 312px, 0 312px);
    background: linear-gradient(120deg, #2b2b2b 0%, #1a1a1a 55%, #242424 100%);
  }
  .machine-photo {
    position: absolute; inset: 0;
    clip-path: polygon(900px 0, 1160px 0, 1160px 362px, 703px 362px);
    background: radial-gradient(ellipse at 70% 55%, #f5f5f5 0%, var(--photo-light) 45%, var(--photo-mid) 100%);
  }
  .brand {
    position: absolute; left: 28px; top: 16px; width: 220px;
  }
  .brand__name {
    font-family: "Oswald", sans-serif; font-weight: 600;
    font-size: 23px; line-height: 1.05; color: var(--ink);
    text-transform: uppercase; letter-spacing: .3px;
  }
  .brand__services {
    margin-top: 6px;
    font-family: "Roboto Condensed", sans-serif; font-weight: 700;
    font-size: 11px; color: var(--ink); letter-spacing: .2px;
  }
  .call {
    position: absolute; left: 292px; top: 20px;
    display: flex; align-items: center; gap: 10px;
  }
  .call__icon { width: 38px; height: 38px; }
  .call__label {
    font-family: "Montserrat", sans-serif; font-weight: 700;
    font-size: 15px; color: var(--yellow); letter-spacing: .4px;
  }
  .call__number {
    font-family: "Montserrat", sans-serif; font-weight: 800;
    font-size: 33px; line-height: 1; color: var(--white); letter-spacing: 1px;
  }
  .headline {
    position: absolute; left: 34px; top: 112px;
    font-family: "Rubik", sans-serif; color: var(--white);
  }
  .headline__lead {
    display: block; font-weight: 600; font-size: 34px; line-height: 1.2;
  }
  .headline__focus {
    display: block; font-weight: 800; font-size: 86px; line-height: 1;
    color: var(--yellow); margin-top: 2px;
  }
  .visit {
    position: absolute; left: 34px; top: 320px;
    display: flex; align-items: baseline; gap: 10px;
    white-space: nowrap;
  }
  .visit__label {
    font-family: "Roboto Condensed", sans-serif; font-weight: 700;
    font-size: 22px; color: var(--yellow);
  }
  .visit__url {
    font-family: "Montserrat", sans-serif; font-weight: 700;
    font-size: 15px; color: var(--ink); letter-spacing: .4px;
  }
</style>
</head>
<body>
  <main class="billboard">
    <div class="site-photo" role="img" aria-label="Dark photo of a multi-storey building under construction"></div>
    <div class="machine-photo" role="img" aria-label="Photo of a yellow backhoe loader in front of a pale construction site"></div>

    <svg class="billboard__shapes" viewBox="0 0 1160 362" aria-hidden="true">
      <polygon points="0,0 270,0 228,88 0,88" fill="var(--yellow)"/>
      <polygon points="282,0 300,0 258,88 240,88" fill="var(--white)"/>
      <polygon points="752,0 792,0 595,362 555,362" fill="var(--ink)"/>
      <polygon points="842,0 884,0 825,108 783,108" fill="var(--yellow)"/>
      <polygon points="560,280 600,280 555,362 515,362" fill="var(--yellow)"/>
    </svg>

    <div class="brand">
      <p class="brand__name">Brindlewood<br>Equipment Company</p>
      <p class="brand__services">EQUIPMENT • TOOLS • DUMPSTERS</p>
    </div>

    <div class="call">
      <svg class="call__icon" viewBox="0 0 40 40" aria-hidden="true">
        <path d="M9 6c2-1 4 0 5 2l3 6c1 2 0 3-1 4l-2 2c1 4 4 7 8 9l2-2c1-1 3-2 4-1l6 3c2 1 3 3 2 5l-2 3c-2 2-5 3-9 1C15 33 7 25 4 16c-2-4-1-7 1-9z" fill="var(--yellow)"/>
        <path d="M22 8a10 10 0 0 1 10 10M22 2a16 16 0 0 1 16 16" fill="none" stroke="var(--yellow)" stroke-width="2.6" stroke-linecap="round"/>
      </svg>
      <div>
        <p class="call__label">CALL US TODAY :</p>
        <p class="call__number">912-730-2591</p>
      </div>
    </div>

    <h1 class="headline">
      <span class="headline__lead">Do You Need</span>
      <span class="headline__lead">Construction Equipment</span>
      <span class="headline__focus">Rental?</span>
    </h1>

    <p class="visit">
      <span class="visit__label">Visit Now:</span>
      <span class="visit__url">www.brindlewoodequipment-example.com</span>
    </p>
  </main>
</body>
</html>
```